Harborline Network Advisors (HNA) Business Card

Front Side, add Company Logo
1.) Harborline Network Advisors
Director of Operations
Delgado, Marco T
(323) 555 0148
782 n Alder Ave Suite 300 PMB2093
Los Angeles, CA 90013
Marco@HarborlineNA.example
www.HarborlineNA.example
2.) Veteran-Owned Business (with Small EGA)

Back Side
- Pictures are ideas of what you can add. The description is what HNA does.
1.) Business Partners:
- Corvalis Business
- KX&L Business
- Tellmora Business
2.) What we do
- Broker of Internet service (partners above)
- Project Management/ Contract Management
- Government Contracts

```html
<!DOCTYPE html>
<html lang="en">
<head>
<meta charset="utf-8">
<title>Harborline Network Advisors – Business Card</title>
<link rel="stylesheet" href="https://fonts.googleapis.com/css2?family=Poppins:wght@400;500;600;700&display=swap">
<style>
  :root {
    --ink: #231f20;
    --gold: #f9b91c;
    --slate: #58585a;
    --paper: #ffffff;
    --stage: #e6e6e6;
    --text-light: #f4f4f4;
    --text-dark: #1d1d1d;
  }
  * { box-sizing: border-box; margin: 0; padding: 0; }
  html, body { width: 686px; height: 1200px; overflow: hidden; }
  body {
    background: var(--stage);
    font-family: "Poppins", sans-serif;
    position: relative;
  }
  .card {
    position: absolute;
    left: 43px;
    width: 600px;
    height: 343px;
    overflow: hidden;
    box-shadow: 0 6px 18px rgba(0,0,0,.22);
  }
  .card--front { top: 200px; background: var(--ink); }
  .card--back { top: 640px; background: var(--ink); }

  /* front */
  .brand-mark {
    position: absolute; left: 40px; top: 70px; width: 210px; height: 180px;
    display: flex; flex-direction: column; align-items: center; justify-content: center;
    color: var(--gold); font-weight: 600; text-align: center;
    font-size: 22px; line-height: 1.2; letter-spacing: 1.5px; text-transform: uppercase;
  }
  .brand-mark__dot {
    width: 34px; height: 34px; border-radius: 50%; background: var(--gold); margin-bottom: 14px;
  }
  .contact { position: absolute; left: 282px; top: 48px; width: 300px; color: var(--text-light); }
  .contact__company { font-size: 16px; font-weight: 600; line-height: 1.2; white-space: nowrap; }
  .contact__name { font-size: 22px; font-weight: 700; color: var(--gold); margin-top: 4px; line-height: 1.25; white-space: nowrap; }
  .contact__title { font-size: 12px; line-height: 1.2; }
  .contact__rule { height: 1px; background: #9a9a9a; width: 252px; margin: 9px 0 12px; }
  .contact__list { list-style: none; font-size: 12px; line-height: 1.3; }
  .contact__item { display: flex; gap: 8px; margin-bottom: 9px; white-space: nowrap; }
  .contact__icon { flex: 0 0 16px; width: 16px; height: 16px; }
  .veteran { position: absolute; left: 286px; top: 260px; display: flex; align-items: center; gap: 10px; color: var(--text-light); font-size: 12px; }
  .veteran__badge { width: 34px; height: 30px; background: #f2f2f2; border-radius: 4px; }
  .front-band { position: absolute; left: 0; bottom: 0; width: 600px; height: 18px; }

  /* back */
  .back__top { position: absolute; left: 0; top: 0; width: 600px; height: 136px; background: var(--paper); }
  .back__wires {
    position: absolute; left: 250px; top: 136px; width: 180px; height: 207px;
    background: radial-gradient(ellipse at 60% 40%, #5a463a 0%, #3a2f2a 45%, var(--ink) 85%);
  }
  .partners-tag {
    position: absolute; left: 24px; top: 27px; height: 31px; padding: 0 24px 0 10px;
    background: var(--gold); color: var(--text-dark); font-size: 18px; font-weight: 500; line-height: 31px;
    clip-path: polygon(0 0, 93% 0, 100% 100%, 0 100%);
  }
  .partners {
    position: absolute; left: 30px; top: 74px; width: 300px;
    display: flex; justify-content: space-between; align-items: center;
  }
  .partner {
    display: flex; align-items: center; gap: 5px;
    font-size: 12px; font-weight: 600; line-height: 1.1; color: var(--text-dark);
  }
  .partner__dot { flex: 0 0 9px; width: 9px; height: 9px; border-radius: 50%; background: var(--text-dark); }
  .services-tag { position: absolute; left: 0; top: 136px; width: 200px; height: 42px; }
  .services-tag__label {
    position: absolute; left: 26px; top: 146px; font-size: 17px; color: var(--text-dark); letter-spacing: .3px;
  }
  .services-tag__label strong { font-weight: 700; }
  .services { position: absolute; left: 26px; top: 206px; list-style: none; color: var(--text-light); font-size: 11.5px; line-height: 1.25; }
  .services__item { display: flex; gap: 6px; margin-bottom: 14px; }
  .services__item strong { font-weight: 600; }
  .services__tick { flex: 0 0 11px; width: 11px; height: 11px; margin-top: 2px; }
  .panel-photo {
    position: absolute; left: 362px; top: 30px; width: 216px; height: 285px;
    border: 2px solid var(--gold);
    background: linear-gradient(180deg, #3a6fc7 0%, #d9dcdf 18%, #c9ccd0 50%, #e3e4e6 80%, #b9bcc0 100%);
  }
</style>
</head>
<body>

<section class="card card--front" aria-label="Business card front">
  <div class="brand-mark">
    <span class="brand-mark__dot"></span>
    Harborline<br>Network<br>Advisors
  </div>

  <div class="contact">
    <p class="contact__company">Harborline Network Advisors</p>
    <p class="contact__name">Delgado, Marco T</p>
    <p class="contact__title">Director of Operations</p>
    <div class="contact__rule"></div>
    <ul class="contact__list">
      <li class="contact__item">
        <svg class="contact__icon" viewBox="0 0 16 16"><rect x="1.5" y="1.5" width="13" height="13" fill="none" stroke="#f9b91c"/><path d="M5 4.5l2 0 .8 2-1.2.9a5 5 0 0 0 2 2l.9-1.2 2 .8v2c-4 .3-7-2.7-6.5-6.5z" fill="#f9b91c"/></svg>
        <span>(323) 555 0148</span>
      </li>
      <li class="contact__item">
        <svg class="contact__icon" viewBox="0 0 16 16"><rect x="1.5" y="1.5" width="13" height="13" fill="none" stroke="#f9b91c"/><path d="M8 3.5a3 3 0 0 0-3 3c0 2.2 3 6 3 6s3-3.8 3-6a3 3 0 0 0-3-3zm0 4.2a1.2 1.2 0 1 1 0-2.4 1.2 1.2 0 0 1 0 2.4z" fill="#f9b91c"/></svg>
        <span>782 n Alder Ave Suite 300 PMB2093<br>Los Angeles, CA 90013</span>
      </li>
      <li class="contact__item">
        <svg class="contact__icon" viewBox="0 0 16 16"><rect x="1.5" y="1.5" width="13" height="13" fill="none" stroke="#f9b91c"/><rect x="4" y="5" width="8" height="6" fill="none" stroke="#f9b91c"/><path d="M4 5l4 3.2L12 5" fill="none" stroke="#f9b91c"/></svg>
        <span>Marco@HarborlineNA.example</span>
      </li>
      <li class="contact__item">
        <svg class="contact__icon" viewBox="0 0 16 16"><rect x="1.5" y="1.5" width="13" height="13" fill="none" stroke="#f9b91c"/><circle cx="8" cy="8" r="3.6" fill="none" stroke="#f9b91c"/><path d="M4.4 8h7.2M8 4.4c-1.6 2-1.6 5.2 0 7.2M8 4.4c1.6 2 1.6 5.2 0 7.2" fill="none" stroke="#f9b91c" stroke-width=".8"/></svg>
        <span>www.HarborlineNA.example</span>
      </li>
    </ul>
  </div>

  <div class="veteran">
    <span>Veteran-Owned Business</span>
    <span class="veteran__badge" role="img" aria-label="Service emblem badge"></span>
  </div>

  <svg class="front-band" viewBox="0 0 600 18" preserveAspectRatio="none" aria-hidden="true">
    <polygon points="0,0 300,0 292,9 300,18 0,18 8,9" fill="#f9b91c"/>
    <polygon points="0,0 8,9 0,18" fill="#231f20"/>
    <polygon points="304,0 600,0 592,9 600,18 304,18 296,9" fill="#58585a"/>
  </svg>
</section>

<section class="card card--back" aria-label="Business card back">
  <div class="back__top"></div>
  <div class="back__wires" role="img" aria-label="Photo of bundled network cables"></div>

  <div class="partners-tag">Business Partners</div>
  <div class="partners">
    <span class="partner"><span class="partner__dot"></span><span>Corvalis<br>Business</span></span>
    <span class="partner"><span class="partner__dot"></span><span>KX&amp;L<br>Business</span></span>
    <span class="partner"><span class="partner__dot"></span><span>Tellmora<br>Business</span></span>
  </div>

  <svg class="services-tag" viewBox="0 0 200 42" aria-hidden="true">
    <polygon points="0,0 190,0 162,38 0,38" fill="#f9b91c"/>
    <polygon points="190,0 200,0 170,42 0,42 0,38 162,38" fill="#ffffff"/>
  </svg>
  <p class="services-tag__label"><strong>WHAT</strong> WE DO</p>

  <ul class="services">
    <li class="services__item">
      <svg class="services__tick" viewBox="0 0 12 12"><circle cx="6" cy="6" r="6" fill="#f9b91c"/><path d="M3.3 6.2l1.8 1.7 3.6-3.6" fill="none" stroke="#231f20" stroke-width="1.5"/></svg>
      <span><strong>Broker of Internet service</strong><br>(partners above)</span>
    </li>
    <li class="services__item">
      <svg class="services__tick" viewBox="0 0 12 12"><circle cx="6" cy="6" r="6" fill="#f9b91c"/><path d="M3.3 6.2l1.8 1.7 3.6-3.6" fill="none" stroke="#231f20" stroke-width="1.5"/></svg>
      <span><strong>Project Management/ Contract<br>Management</strong></span>
    </li>
    <li class="services__item">
      <svg class="services__tick" viewBox="0 0 12 12"><circle cx="6" cy="6" r="6" fill="#f9b91c"/><path d="M3.3 6.2l1.8 1.7 3.6-3.6" fill="none" stroke="#231f20" stroke-width="1.5"/></svg>
      <span><strong>Government Contracts</strong></span>
    </li>
  </ul>

  <div class="panel-photo" role="img" aria-label="Photo of an electrical distribution panel with breakers and wiring"></div>
</section>

</body>
</html>
```